コンペの提出はファーストビューのみでも大丈夫です。
金額はLP全てのデザイン分です。
納品はXDもしくはPSDでお願いいたします。

【ターゲット】
30-50代の男女向け 男女比率 女性7:男性3

【デザインテイストについて】
反響の良かったチラシをベースに原稿制作しました。
添付しておきますのでデザインテイストについても参考にしていただいて問題ありません。

その他デザイン参考サイト
https://lumora-works.co.jp/career-tag/occupation/r50_a

【写真素材】
https://files.quillbox-share.com/box/folders/7kQmZtRwPaLsXeVnBcYuHgDfJoIpTrEsW?usp=sharing

足りない写真素材はケルナフォトバンクなどを使用してください
ロゴデータは添付してあります
1ページ
青系
原稿兼WFを添付します。

WFについては目安として考えていただき、デザインアイデアで変更していただいても大丈夫です。

要望通りのデザインを作成していただきありがとうございました!

限られた時間の中で多くのご提案をいただきまして本当にありがとうございました。
また機会がありましたらよろしくお願いいたします。

```html
<!DOCTYPE html>
<html lang="ja">
<head>
<meta charset="UTF-8">
<title>登録ヘルパー大募集</title>
<link href="https://fonts.googleapis.com/css2?family=Noto+Sans+JP:wght@400;500;700;900&display=swap" rel="stylesheet">
<style>
:root{
  --sky:#d9eef8;
  --sky-deep:#a9d8ef;
  --blue:#1f7fc4;
  --navy:#1a3f6e;
  --red:#e8293b;
  --ink:#2a3441;
  --card:#e4eef6;
  --white:#ffffff;
  --gray:#f3f5f7;
}
*{margin:0;padding:0;box-sizing:border-box}
html,body{width:691px;height:1200px;overflow:hidden}
body{font-family:"Noto Sans JP",sans-serif;color:var(--ink);background:var(--white);position:relative}
.hero{position:absolute;left:0;top:0;width:691px;height:360px;background:linear-gradient(160deg,var(--white) 0%,var(--sky) 45%,var(--sky-deep) 100%);overflow:hidden}
.hero-photo{position:absolute;left:0;top:40px;width:300px;height:320px;background:linear-gradient(180deg,#bfe0ef,#6fb0c9 60%,#3f8fae)}
.brand{position:absolute;left:14px;top:12px;display:flex;align-items:center;gap:6px;font-weight:700;font-size:17px;color:var(--blue)}
.brand-dot{width:14px;height:14px;border-radius:50%;background:var(--blue)}
.area{position:absolute;right:40px;top:20px;background:var(--navy);color:var(--white);font-size:11px;font-weight:700;padding:4px 10px;line-height:1.45;text-align:center;width:165px}
.direct{position:absolute;right:40px;top:62px;font-size:26px;font-weight:900;color:var(--navy);letter-spacing:1px;line-height:1.3}
.title-sub{position:absolute;left:100px;top:82px;font-size:38px;font-weight:900;color:var(--red);letter-spacing:2px;line-height:1.2}
.title-main{position:absolute;left:300px;top:118px;font-size:78px;font-weight:900;color:var(--navy);letter-spacing:2px;line-height:1}
.wage{position:absolute;left:470px;top:206px;width:195px;background:var(--white);font-size:11px;font-weight:700;color:var(--navy);line-height:1.5;padding:3px 8px}
.wage b{color:var(--red);font-size:13px}
.pills{position:absolute;left:140px;top:254px;display:flex;flex-wrap:wrap;gap:6px;width:430px}
.pill{width:138px;text-align:center;background:var(--blue);color:var(--white);font-size:11px;font-weight:700;padding:4px 0;border-radius:4px;line-height:1.4}
.allok{position:absolute;left:140px;top:308px;font-size:42px;font-weight:900;color:var(--red);letter-spacing:2px;line-height:1.1}
.allok-note{position:absolute;left:380px;top:318px;background:var(--white);color:var(--navy);font-size:15px;font-weight:700;padding:4px 12px;border-radius:4px;line-height:1.4}
.strip{position:absolute;left:0;top:360px;width:691px;height:62px;display:flex;gap:3px;background:var(--white)}
.strip div{flex:1;background:linear-gradient(180deg,#e3edf3,#9cbdcf)}
.worries{position:absolute;left:0;top:422px;width:691px;height:778px;background:var(--white)}
.worries-head{position:absolute;left:0;top:24px;width:691px;text-align:center}
.worries-head h2{font-size:30px;font-weight:900;color:var(--navy);line-height:1.4}
.worries-head h2 em{font-style:normal;color:var(--red);font-size:40px;border-bottom:4px solid var(--red)}
.worries-head p{margin-top:10px;font-size:15px;font-weight:700;color:var(--navy)}
.case{position:absolute;width:540px;height:104px;background:var(--card);border-radius:6px;padding:16px 22px}
.case h3{font-size:19px;font-weight:700;color:var(--ink);border-bottom:1px dashed #9ab;padding-bottom:8px;line-height:1.4}
.case p{margin-top:8px;font-size:11px;line-height:1.55}
.case p b{color:var(--red)}
.case-a{left:100px;top:125px}
.case-b{left:50px;top:255px}
.case-c{left:100px;top:385px}
.avatar{position:absolute;width:85px;height:85px;border-radius:50%;background:linear-gradient(180deg,#fbe2bf,#f2a65a)}
.av-a{left:20px;top:120px}.av-b{left:595px;top:260px}.av-c{left:20px;top:380px}
</style>
</head>
<body>
<section class="hero">
  <div class="hero-photo" role="img" aria-label="車いすの利用者と介護スタッフの写真"></div>
  <div class="brand"><span class="brand-dot"></span>ケアそよか</div>
  <div class="area">宜野湾・浦添・うるま・中城<br>・沖縄・北谷周辺</div>
  <div class="direct">直行直帰</div>
  <div class="title-sub">登録ヘルパー</div>
  <div class="title-main">大募集!</div>
  <div class="wage">時給 6:00～18:00 <b>1,500円</b><br>18:00～翌6:00 <b>1,875円</b></div>
  <div class="pills">
    <span class="pill">月収35万円以上希望</span>
    <span class="pill">扶養の範囲内で働きたい</span>
    <span class="pill">身体介護は避けたい</span>
    <span class="pill">夜間だけワークしたい</span>
    <span class="pill">希望の日に働きたい</span>
  </div>
  <div class="allok">全部OK!</div>
  <div class="allok-note">都合に合わせて働けます</div>
</section>
<div class="strip">
  <div role="img" aria-label="スタッフ集合写真"></div>
  <div role="img" aria-label="研修の様子の写真"></div>
  <div role="img" aria-label="介護の様子の写真"></div>
  <div role="img" aria-label="事務所の様子の写真"></div>
</div>
<section class="worries">
  <div class="worries-head">
    <h2>あなたの<em>都合</em>はどれ？</h2>
    <p>いろんな都合を聞かせてください！</p>
  </div>
  <div class="case case-a"><h3>家事ならできるけれど身体介護はちょっと不安</h3><p><b>家事サービスのみの方も大歓迎！</b>身体介護を行わなくても時給は同じです♪</p></div>
  <div class="avatar av-a" role="img" aria-label="考える女性のイラスト"></div>
  <div class="case case-b"><h3>子供が学校に行っているあいだだけ働きたい</h3><p><b>24時間の中で1日1時間〜OK！</b>残業一切なしだから子どもの帰宅時間や習い事の時間に合わせて勤務できます。</p></div>
  <div class="avatar av-b" role="img" aria-label="考える女性のイラスト"></div>
  <div class="case case-c"><h3>家事ならできるけれど身体介護はちょっと不安</h3><p><b>家事サービスのみの方も大歓迎！</b>身体介護を行わなくても時給は同じです♪</p></div>
  <div class="avatar av-c" role="img" aria-label="考える女性のイラスト"></div>
</section>
</body>
</html>
```